Dozy Wren sleep comforter 'Local campaign' Billboard design

Billboard will be on display in a busy local street of Coburg. We want this to appeal to the fact that we are locals, we are mums, we care about mums, our factory is here, our staff are here and we support the community here. We like a possible support angle through the isolation of covid. For the purpose of design please refer to our:
Facebook: https://www.facebook.com/dozywrennaptoys
Insta: https://www.instagram.com/dozywren_naptoys
Or www.dozywrenhome.example

Designs look the same

```html
<!DOCTYPE html>
<html lang="en">
<head>
<meta charset="utf-8">
<title>Dozy Wren – Quiet is Comfort Billboard</title>
<link rel="stylesheet" href="https://fonts.googleapis.com/css2?family=Anton&family=Inter:wght@400;700&display=swap">
<style>
  :root {
    --wall: #e9e8e6;
    --ink: #0b0b0b;
    --cocoa: #a5673f;
    --plush-tan: #c99a66;
    --plush-light: #dcb88c;
    --plush-cream: #f4f1ec;
  }
  * { margin: 0; padding: 0; box-sizing: border-box; }
  html, body { width: 1200px; height: 672px; overflow: hidden; background: var(--wall); }
  .billboard {
    position: relative;
    width: 1200px;
    height: 672px;
    overflow: hidden;
    background: var(--wall);
  }
  .product-photo {
    position: absolute;
    left: 500px;
    top: 0;
    width: 700px;
    height: 672px;
    background:
      radial-gradient(ellipse 230px 200px at 540px 440px, var(--plush-cream) 0%, var(--plush-cream) 60%, rgba(244,241,236,0) 100%),
      radial-gradient(ellipse 520px 620px at 600px 300px, var(--plush-tan) 0%, var(--plush-light) 55%, rgba(220,184,140,0) 80%),
      radial-gradient(ellipse 400px 200px at 360px 640px, var(--plush-light) 0%, rgba(220,184,140,0) 80%);
  }
  .brand-name {
    position: absolute;
    left: 120px;
    top: 141px;
    width: 120px;
    font-family: "Anton", sans-serif;
    font-size: 20px;
    line-height: 26px;
    color: var(--ink);
    text-align: center;
    white-space: nowrap;
  }
  .headline {
    font-family: "Anton", sans-serif;
    font-weight: 400;
    line-height: 1;
  }
  .headline-lead,
  .headline-key {
    position: absolute;
    left: 72px;
    white-space: nowrap;
    transform-origin: left center;
    transform: skewY(2deg);
  }
  .headline-lead {
    top: 199px;
    font-size: 97px;
    color: var(--ink);
    letter-spacing: -0.5px;
  }
  .headline-key {
    top: 321px;
    font-size: 156px;
    color: var(--cocoa);
    text-transform: uppercase;
    letter-spacing: -1px;
  }
  .body-copy {
    position: absolute;
    left: 79px;
    top: 544px;
    width: 540px;
    font-family: "Inter", sans-serif;
    font-size: 12.4px;
    line-height: 17px;
    color: var(--ink);
  }
  .body-copy strong { font-weight: 700; }
</style>
</head>
<body>
  <main class="billboard">
    <div class="product-photo" role="img" aria-label="Close-up photo of a soft tan plush bear comforter with a cream muzzle"></div>
    <div class="brand-name">Dozy Wren</div>
    <h1 class="headline">
      <span class="headline-lead">quiet is</span>
      <span class="headline-key">comfort</span>
    </h1>
    <p class="body-copy">
      If <strong>SLEEP</strong> makes babies happy then our toy teaches babies to fall in love with sleep.<br>
      See why they work and why they are Australia’s #1 selling and rated comforter by<br>
      visiting <strong>www.dozywrenhome.example.</strong>
    </p>
  </main>
</body>
</html>
```